Dean wants a Kick arse Business card

Launching my new company Harrow Real Estate 1st July, and will be mailing out to past clients, need a kick arse business card design pronto to get printing done in time for mail out
I'm after a two sided card - one side for all contact details (see below) the other side for impact (kick arsery!)
Logo and my photo attached, details to go onto card are as follows
Dean Harrow - Principal
M: 0412 905 364
E: dean@harrowre.com.au
Dean Harrow Real Estate Pty Ltd trading as Harrow Real Estate
Licensed Real Estate & Business Agents
ABN 42 803 517 296 Triennial Cert No. RA31472
14 Marbrook Avenue, Kelmscott WA 6111
Tel: 08 9371 6048 Fax: 08 6209 4812

```html
<!DOCTYPE html>
<html lang="en">
<head>
<meta charset="utf-8">
<title>Harrow Real Estate – Business Card</title>
<link rel="stylesheet" href="https://fonts.googleapis.com/css2?family=Open+Sans:wght@400;600&display=swap">
<style>
  :root {
    --page-bg: #eceae4;
    --card-bg: #ffffff;
    --band-light: #4f7bc4;
    --band-dark: #24407a;
    --brand-blue: #2d4f8f;
    --text-main: #3c3f48;
    --text-soft: #6a6e78;
    --photo-tone: linear-gradient(160deg, #c9a58c 0%, #6e6a6a 55%, #1f1f24 100%);
  }
  * { box-sizing: border-box; margin: 0; padding: 0; }
  html, body {
    width: 1200px; height: 800px; overflow: hidden;
    background: var(--page-bg);
    font-family: "Open Sans", Arial, sans-serif;
    color: var(--text-main);
  }
  .canvas {
    position: relative; width: 1200px; height: 800px;
    display: flex; flex-direction: column; align-items: center; justify-content: center; gap: 32px;
  }
  .card {
    position: relative; width: 640px; height: 350px;
    background: var(--card-bg);
    box-shadow: 0 6px 18px rgba(0,0,0,0.18);
    overflow: hidden;
  }
  .card__band-top { position: absolute; left: 0; right: 0; top: 0; height: 12px; background: var(--band-light); }
  .card__band-bottom { position: absolute; left: 0; right: 0; bottom: 0; height: 34px; background: var(--band-dark); }

  .brand { display: flex; align-items: center; gap: 12px; }
  .brand__dot { width: 30px; height: 30px; border-radius: 50%; background: var(--brand-blue); flex: none; }
  .brand__name { font-weight: 600; font-size: 28px; line-height: 1; color: var(--brand-blue); white-space: nowrap; }

  /* Details side */
  .card--details .brand { position: absolute; top: 58px; left: 0; right: 0; justify-content: center; }
  .legal {
    position: absolute; top: 140px; left: 0; right: 0; text-align: center;
    font-size: 11.5px; line-height: 1.55; color: var(--text-main);
  }
  .contact-row {
    position: absolute; left: 40px; right: 40px; top: 230px;
    display: flex; justify-content: space-between; align-items: flex-start;
    font-size: 11.5px; line-height: 1.45;
  }
  .contact { display: flex; align-items: flex-start; gap: 8px; }
  .icon { width: 18px; height: 18px; flex: none; }

  /* Personal side */
  .card--personal .brand { position: absolute; left: 50px; top: 195px; }
  .card--personal .brand__name { font-size: 30px; }
  .portrait {
    position: absolute; left: 340px; top: 95px; width: 72px; height: 72px; border-radius: 50%;
    background: var(--photo-tone);
  }
  .person { position: absolute; left: 432px; top: 76px; display: flex; flex-direction: column; gap: 12px; font-size: 13px; }
  .person .contact { align-items: center; gap: 12px; }
  .person__name { display: flex; flex-direction: column; line-height: 1.3; }
  .person__role { font-size: 11px; color: var(--text-soft); }
</style>
</head>
<body>
<main class="canvas">

  <section class="card card--details" aria-label="Card side with company details">
    <div class="card__band-top"></div>
    <div class="brand">
      <span class="brand__dot"></span>
      <span class="brand__name">Harrow Real Estate</span>
    </div>
    <div class="legal">
      <p>Dean Harrow Real Estate Pty Ltd trading as Harrow Real Estate</p>
      <p>Licensed Real Estate &amp; Business Agents</p>
      <p>ABN 42 803 517 296 &nbsp;&nbsp;•&nbsp;&nbsp; Triennial Cert No. RA31472</p>
    </div>
    <div class="contact-row">
      <div class="contact">
        <svg class="icon" viewBox="0 0 18 18"><circle cx="9" cy="9" r="8" fill="none" stroke="var(--brand-blue)" stroke-width="1.3"/><path d="M9 4.5a3 3 0 0 1 3 3c0 2.2-3 5.8-3 5.8S6 9.7 6 7.5a3 3 0 0 1 3-3z" fill="var(--brand-blue)"/><circle cx="9" cy="7.5" r="1" fill="#fff"/></svg>
        <span>14 Marbrook Avenue,<br>Kelmscott WA 6111</span>
      </div>
      <div class="contact">
        <svg class="icon" viewBox="0 0 18 18"><circle cx="9" cy="9" r="8" fill="none" stroke="var(--brand-blue)" stroke-width="1.3"/><path d="M6 4.8l1.6-.3 1 2.2-1 .8a6 6 0 0 0 2.7 2.7l.8-1 2.2 1-.3 1.6c-3.8.3-7.3-3.2-7-7z" fill="var(--brand-blue)"/></svg>
        <span>08 9371 6048</span>
      </div>
      <div class="contact">
        <svg class="icon" viewBox="0 0 18 18"><circle cx="9" cy="9" r="8" fill="none" stroke="var(--brand-blue)" stroke-width="1.3"/><rect x="5.5" y="7" width="7" height="4.5" rx="0.8" fill="var(--brand-blue)"/><rect x="7" y="4.5" width="4" height="2.5" fill="none" stroke="var(--brand-blue)"/><rect x="7" y="11" width="4" height="2.5" fill="#fff" stroke="var(--brand-blue)"/></svg>
        <span>Fax: 08 6209 4812</span>
      </div>
    </div>
    <div class="card__band-bottom"></div>
  </section>

  <section class="card card--personal" aria-label="Card side with personal contact">
    <div class="card__band-top"></div>
    <div class="brand">
      <span class="brand__dot"></span>
      <span class="brand__name">Harrow Real Estate</span>
    </div>
    <div class="portrait" role="img" aria-label="Portrait photo of Dean Harrow"></div>
    <div class="person">
      <div class="contact">
        <svg class="icon" viewBox="0 0 18 18"><circle cx="9" cy="9" r="8" fill="none" stroke="var(--brand-blue)" stroke-width="1.3"/><circle cx="9" cy="7" r="2.2" fill="var(--brand-blue)"/><path d="M5 13.2c.6-2.2 2.2-3.2 4-3.2s3.4 1 4 3.2z" fill="var(--brand-blue)"/></svg>
        <span class="person__name">Dean Harrow<span class="person__role">Principal</span></span>
      </div>
      <div class="contact">
        <svg class="icon" viewBox="0 0 18 18"><circle cx="9" cy="9" r="8" fill="none" stroke="var(--brand-blue)" stroke-width="1.3"/><path d="M6 4.8l1.6-.3 1 2.2-1 .8a6 6 0 0 0 2.7 2.7l.8-1 2.2 1-.3 1.6c-3.8.3-7.3-3.2-7-7z" fill="var(--brand-blue)"/></svg>
        <span>0412 905 364</span>
      </div>
      <div class="contact">
        <svg class="icon" viewBox="0 0 18 18"><circle cx="9" cy="9" r="8" fill="none" stroke="var(--brand-blue)" stroke-width="1.3"/><rect x="5" y="6" width="8" height="6" rx="0.8" fill="var(--brand-blue)"/><path d="M5.3 6.4L9 9.3l3.7-2.9" fill="none" stroke="#fff" stroke-width="0.9"/></svg>
        <span>dean@harrowre.com.au</span>
      </div>
    </div>
    <div class="card__band-bottom"></div>
  </section>

</main>
</body>
</html>
```